BRWK branding
Stationery & misc. Design Elements
Thank Delphine!
To all designers: My client has chosen Orvo Design as the winner on this project. Thanks to all for the hard work and revised designs. Keep an eye out for another project for Birchwood Spinal Care Logo. Thanks for the efforts.
Delphine
@ Brambly : I think some of your winning designs(concept) are similar....
So,are these copied from others???
No,Dear Friend,Everything is separate from others as like as me.
Don't be upset... :)
Wishing you all the best.
-A Friend,
OrvoDesigner
http://www.draftvane.example/drafts/display/contest/10001/draft/300001
http://www.draftvane.example/drafts/display/contest/10002/draft/300002
http://www.draftvane.example/drafts/display/contest/10003/draft/300003
http://www.draftvane.example/drafts/display/contest/10004/draft/300004
http://www.draftvane.example/drafts/display/contest/10005/draft/300005
http://www.draftvane.example/drafts/display/contest/10006/draft/300006
http://www.draftvane.example/drafts/display/contest/10007/draft/300007
@ Dear Brambly : Yes,I already won that contest. I think - you guess something similar like that. Would you compare again ,please? It is not copied from that.Please,See carefully Envelope and the Letterhead again(that you thinking).
Only the color format are similar that I like most.Without this everything is different(about the color code,Color area,address position,watermark,line and the logo position).Is it clear,dear?
Thanks for your hard trying about the design.
I really wish your success.
(A Competitor and a friend.)
-OrvoDesigner
Orvo Design,
u already winning this design
To all designers: remember to submit a page or so of additional design elements for use in future marketing collateral - as stated in
the project brief. Thanks
Correction ** New logo uploaded 11/15
Please upload ai or eps of your logo.

```html
<!DOCTYPE html>
<html lang="en">
<head>
<meta charset="utf-8">
<title>BRWK Stationery</title>
<link rel="stylesheet" href="https://fonts.googleapis.com/css2?family=Marcellus&display=swap">
<style>
  :root {
    --paper: #ffffff;
    --board: #ffffff;
    --frame: #c9c9c9;
    --brand: #1f5fae;
    --brand-deep: #0f4a95;
    --brand-light: #5aa2e0;
    --shadow: rgba(0, 0, 0, 0.35);
  }
  * { box-sizing: border-box; margin: 0; padding: 0; }
  html, body { width: 1200px; height: 919px; overflow: hidden; background: var(--board); }
  body { position: relative; font-family: "Marcellus", serif; color: var(--brand); }

  .board-frame {
    position: absolute; left: 42px; top: 18px; width: 1116px; height: 864px;
    border: 1px solid var(--frame);
  }
  .sheet {
    position: absolute; background: var(--paper); overflow: hidden;
    box-shadow: 4px 6px 10px var(--shadow);
  }
  .letterhead { left: 405px; top: 68px; width: 600px; height: 782px; border: 1px solid #d6d6d6; }
  .envelope { left: 70px; top: 375px; width: 670px; height: 293px; border: 1px solid #555; }
  .business-card { left: 875px; top: 250px; width: 255px; height: 155px; border: 1px solid #cfcfcf; }

  .corner-tone {
    position: absolute; top: 0; right: 0;
    background: linear-gradient(to bottom left, var(--brand-deep) 0%, var(--brand-light) 30%, rgba(255,255,255,0) 65%);
  }
  .letterhead .corner-tone { width: 260px; height: 180px; }
  .envelope .corner-tone { width: 250px; height: 150px; }
  .business-card .corner-tone { width: 100px; height: 75px; }

  .brand-name {
    display: flex; align-items: center; gap: 6px;
    font-size: 17px; color: var(--brand); white-space: nowrap; letter-spacing: 0.3px;
  }
  .brand-dot { width: 11px; height: 11px; border-radius: 50%; background: var(--brand); flex: none; }
  .address { font-size: 8.5px; letter-spacing: 0.5px; color: var(--brand); margin-top: 22px; }

  .letterhead .brand-block { position: absolute; left: 20px; top: 52px; }
  .envelope .brand-block { position: absolute; left: 10px; top: 48px; }

  .business-card .brand-block { position: absolute; left: 12px; top: 40px; }
  .business-card .brand-name { font-size: 9px; gap: 4px; }
  .business-card .brand-dot { width: 7px; height: 7px; }
  .card-details { position: absolute; left: 12px; top: 92px; font-size: 5.5px; line-height: 1.5; letter-spacing: 0.3px; }
  .card-details .person { font-size: 6.5px; }
  .card-details .contact { margin-top: 8px; }
</style>
</head>
<body>
  <div class="board-frame"></div>

  <section class="sheet letterhead">
    <div class="corner-tone" role="img" aria-label="Blue curved corner band"></div>
    <div class="brand-block">
      <div class="brand-name"><span class="brand-dot"></span>Birchwood Spinal Care</div>
      <p class="address">214 FENWICK LANE, ALDER, NJ 07990</p>
    </div>
  </section>

  <section class="sheet envelope">
    <div class="corner-tone" role="img" aria-label="Blue curved corner band"></div>
    <div class="brand-block">
      <div class="brand-name"><span class="brand-dot"></span>Birchwood Spinal Care</div>
      <p class="address">214 FENWICK LANE, ALDER, NJ 07990</p>
    </div>
  </section>

  <section class="sheet business-card">
    <div class="corner-tone" role="img" aria-label="Blue curved corner band"></div>
    <div class="brand-block">
      <div class="brand-name"><span class="brand-dot"></span>Birchwood Spinal Care</div>
    </div>
    <div class="card-details">
      <p class="person">MARLO VENN, M.D.</p>
      <p>Medical Director, Spine Care</p>
      <p class="contact">214 FENWICK LANE, ALDER, NJ 07990</p>
      <p>info@birchwoodspine.example</p>
    </div>
  </section>
</body>
</html>
```